Design Business Cards for Novarin Education & Trading Company

Dear Designers,

We are looking for a Clean, Classy, Unique, Luxury and professional design for business cards & simple letter head for a Novarin Education & Trading. Please see the attached image for our logo. We like the black on the side of the card, but by all means be creative. You can also play around with the logo.
We prefer gold foil stamping, but it is not really necessary.

Feel free to submit as many entries as you want to increase your chance of winning. DO NOT submit something we can actually do it ourselves, e.g. free online generator, copying and pasting our logo on somehing plain without actually designing anything

For Business Card

• The card will be double sided with following detail appear.

-Name,
-Position,
-Address,
-Phone number,
-Email address
-and Website URL
• Business Card size, direction(horizontal or vertical) & shape is open to designer creativity.

For Letterhead
Design
• Should be matching colour theme of Logo/Business card.

Others;
• Winner need to provide layered PSD & ai files for all designs including fonts, colours used and any additional related documents and files.
• Attached is the logo (must be used in design)
• Building a website and brochures that will be further selling points to the winner, for our next business development.

Thanks for all your entries!

```html
<!DOCTYPE html>
<html lang="en">
<head>
<meta charset="utf-8">
<title>Novarin Education &amp; Trading — Stationery</title>
<link rel="stylesheet" href="https://fonts.googleapis.com/css2?family=Cinzel:wght@500&family=Montserrat:wght@400;600&display=swap">
<style>
  :root {
    --backdrop: #e9e9e9;
    --paper: #ffffff;
    --ink: #1c1c1c;
    --gold: #e0a417;
    --gold-deep: #c98c0c;
    --grey: #8a8a8a;
    --url-grey: #b5b5b5;
  }
  * { margin: 0; padding: 0; box-sizing: border-box; }
  html, body { width: 1200px; height: 800px; overflow: hidden; }
  body {
    background: var(--backdrop);
    position: relative;
    font-family: "Montserrat", sans-serif;
  }

  /* Letterhead */
  .letterhead {
    position: absolute; left: 70px; top: 40px;
    width: 509px; height: 720px;
    background: var(--paper);
    box-shadow: 0 2px 10px rgba(0,0,0,.12);
    overflow: hidden;
  }
  .letterhead__band {
    height: 118px; background: var(--ink);
    display: flex; flex-direction: column; align-items: center; justify-content: center;
  }
  .letterhead__footer { position: absolute; left: 0; bottom: 0; width: 509px; height: 240px; }
  .letterhead__url {
    font-family: "Montserrat", sans-serif; font-size: 14px; letter-spacing: 1.2px;
    fill: var(--url-grey);
  }

  .brand { display: flex; flex-direction: column; align-items: center; gap: 8px; }
  .brand__dot { width: 22px; height: 22px; border-radius: 50%; background: var(--gold); }
  .brand__name {
    font-family: "Cinzel", serif; font-weight: 500; color: var(--gold);
    letter-spacing: .18em; font-size: 15px;
  }

  /* Business cards */
  .card {
    position: absolute; left: 640px; width: 500px; height: 286px;
    box-shadow: 0 2px 10px rgba(0,0,0,.14);
    overflow: hidden;
  }
  .card--front { top: 70px; background: var(--ink); border-bottom: 12px solid var(--gold); display: flex; align-items: center; justify-content: center; }
  .card--front .brand__dot { width: 40px; height: 40px; }
  .card--front .brand__name { font-size: 26px; }

  .card--back { top: 420px; background: var(--paper); }
  .card__accent {
    position: absolute; left: 40px; top: 58px;
    width: 170px; height: 170px; border-radius: 50%;
    background: linear-gradient(135deg, var(--gold), var(--gold-deep));
  }
  .card__details { position: absolute; left: 262px; top: 52px; }
  .card__name {
    font-family: "Cinzel", serif; font-weight: 500; color: var(--gold);
    font-size: 17px; letter-spacing: .06em;
  }
  .card__role { font-size: 10px; color: var(--grey); margin-top: 3px; }
  .card__contacts { list-style: none; margin-top: 22px; }
  .card__contacts li {
    display: flex; align-items: center; gap: 9px;
    font-size: 10px; color: #555; line-height: 1.25; margin-bottom: 8px;
  }
  .card__contacts svg { width: 11px; height: 11px; flex: none; fill: var(--gold); }
  .card__address { display: flex; flex-direction: column; }
</style>
</head>
<body>

<section class="letterhead" aria-label="Letterhead">
  <header class="letterhead__band">
    <div class="brand">
      <span class="brand__dot"></span>
      <span class="brand__name">NOVARIN</span>
    </div>
  </header>

  <svg class="letterhead__footer" viewBox="0 0 509 240">
    <path d="M0,240 L0,230 C220,226 360,64 509,38 L509,240 Z" fill="#1c1c1c"/>
    <path d="M0,224 C220,220 360,58 509,32" fill="none" stroke="#e0a417" stroke-width="4"/>
    <text class="letterhead__url" x="490" y="156" text-anchor="end">www.novarinedu.com</text>
  </svg>
</section>

<section class="card card--front" aria-label="Business card front">
  <div class="brand">
    <span class="brand__dot"></span>
    <span class="brand__name">NOVARIN</span>
  </div>
</section>

<section class="card card--back" aria-label="Business card back">
  <span class="card__accent"></span>
  <div class="card__details">
    <p class="card__name">MARISOL T. AVEREY</p>
    <p class="card__role">Head Designer</p>
    <ul class="card__contacts">
      <li>
        <svg viewBox="0 0 12 12"><path d="M6 0a4 4 0 0 0-4 4c0 3 4 8 4 8s4-5 4-8a4 4 0 0 0-4-4zm0 5.5A1.5 1.5 0 1 1 6 2.5a1.5 1.5 0 0 1 0 3z"/></svg>
        <span class="card__address"><span>12 Harbor Lane, Suite 4</span><span>Westfield, NY 10234</span></span>
      </li>
      <li>
        <svg viewBox="0 0 12 12"><path d="M3 0l2 3-1.2 1.3a7 7 0 0 0 3.9 3.9L9 7l3 2-1.2 2.4C5 11.5.5 7 .6 1.2z"/></svg>
        <span>+1 555 014 2290</span>
      </li>
      <li>
        <svg viewBox="0 0 12 12"><path d="M0 2h12v8H0zM1 3l5 3.5L11 3v-.5H1z" fill-rule="evenodd"/></svg>
        <span>hello@novarinedu.com</span>
      </li>
      <li>
        <svg viewBox="0 0 12 12"><circle cx="6" cy="6" r="5.5"/></svg>
        <span>www.novarinedu.com</span>
      </li>
    </ul>
  </div>
</section>

</body>
</html>
```